Creative Real Estate Listing Mailer

I would like a creative double sided Real Estate listing flier/mailer to send out enticing people to list their house for sale with me. An example in my head, but feel free to be creative,.. would be one side with a Weiner dog with a sack of money on its back saying something like " its time to cash in" and the other side having some kind of southwest backdrop ( I live in Arizona) or luxury home, with my photo and my contact info saying something like list your house with me, or see what your home is worth etc.

Target Market(s)

People interested in selling their homes

Industry/Entity Type

Real Estate Agent

Contact Information for Business Card

Similar to the flyer, but simpler

Requirements
Must have
• My name: Milo Trask
My Email: milotrask@brevlo.com
My Phone# (480) 555 0147
Website www.Milotrask.com

```html
<!DOCTYPE html>
<html lang="en">
<head>
<meta charset="utf-8">
<title>Listing Mailer – Milo Trask</title>
<link href="https://fonts.googleapis.com/css2?family=Titillium+Web:wght@600;700&family=Open+Sans:wght@400;600&family=Playball&display=swap" rel="stylesheet">
<style>
  :root{
    --navy:#0f2a6b;
    --blue:#2a4fb0;
    --blue-light:#3a63c8;
    --red:#c8202f;
    --white:#ffffff;
    --grey:#e4e4e6;
    --ink:#2b2b2b;
    --line:#b9b9bd;
    --bg:#f1f0ee;
  }
  *{margin:0;padding:0;box-sizing:border-box}
  html,body{width:1066px;height:1200px;overflow:hidden;background:var(--bg)}
  .canvas{position:relative;width:1066px;height:1200px}
  .card{position:absolute;left:183px;width:700px;height:500px;background:var(--white);overflow:hidden;box-shadow:0 4px 14px rgba(0,0,0,.18)}
  .card--front{top:60px}
  .card--back{top:630px}
  .card svg.shapes{position:absolute;inset:0}
  .headline{position:absolute;left:22px;top:56px;font:700 38px/50px "Titillium Web",sans-serif;color:var(--white);letter-spacing:-.3px}
  .headline-rule{position:absolute;left:22px;top:165px;width:137px;height:2px;background:var(--white)}
  .offer{position:absolute;left:22px;top:186px;font:400 24px/32px "Open Sans",sans-serif;color:var(--white);letter-spacing:-.2px}
  .offer-agent{position:absolute;left:20px;top:253px;font:400 16px "Playball",cursive;color:#d8def0}
  .cash-banner{position:absolute;left:398px;top:340px;width:252px;height:34px;color:var(--white);font:700 22px/34px "Titillium Web",sans-serif;text-align:center}
  .brand{position:absolute;display:flex;align-items:center;gap:10px;font-family:"Open Sans",sans-serif;font-weight:600;color:var(--ink);letter-spacing:2px;text-transform:uppercase;white-space:nowrap}
  .brand-mark{background:var(--red);flex:none}
  .brand--front{left:16px;top:382px;font-size:21px}
  .brand--front .brand-mark{width:50px;height:50px}
  .brand--back{left:428px;top:50px;font-size:9.5px;letter-spacing:.5px;gap:7px}
  .brand--back .brand-mark{width:18px;height:18px}
  .socials{position:absolute;right:14px;top:424px;display:flex;gap:3px}
  .socials span{width:21px;height:21px;border-radius:50%;background:var(--blue)}
  .contact-bar{position:absolute;left:0;top:456px;width:700px;height:35px;background:var(--red);display:flex;justify-content:space-between;align-items:center;padding:0 17px 0 26px;font:600 16px "Open Sans",sans-serif;color:var(--white);letter-spacing:.3px}
  .contact-bar .item{display:flex;align-items:center;gap:8px}
  .icon{width:15px;height:15px;flex:none}
  .back-photo{position:absolute;left:0;top:0;width:470px;height:183px;background:linear-gradient(180deg,#c9d4dc 0%,#a89a88 45%,#6e8a94 75%,#3fa6c9 100%)}
  .agent-panel{position:absolute;left:0;top:197px;width:380px;height:228px;background:var(--grey)}
  .agent-photo{position:absolute;left:0;top:140px;width:155px;height:285px;background:linear-gradient(180deg,#d8cfc6 0%,#b89a82 22%,#2a3346 40%,#1c2436 100%)}
  .pitch{position:absolute;left:160px;top:218px;font:700 21px/23px "Titillium Web",sans-serif;color:var(--blue)}
  .agent-name{position:absolute;left:160px;top:298px;font:400 24px "Playball",cursive;color:var(--red)}
  .agent-contact{position:absolute;left:162px;top:332px;font:400 13px/17px "Open Sans",sans-serif;color:var(--blue)}
  .agent-contact .item{display:flex;align-items:center;gap:7px}
  .agent-contact .icon{width:12px;height:12px}
  .badges{position:absolute;left:162px;top:384px;display:flex;gap:10px;align-items:center}
  .badge-wide{width:68px;height:30px;border:2px solid var(--navy);background:#dfe4f2}
  .badge-square{width:32px;height:32px;background:var(--ink)}
  .web-bar{position:absolute;left:0;top:430px;width:380px;height:70px;background:linear-gradient(90deg,var(--navy),#1c3c92 75%,#4a6ac4)}
  .web-text{position:absolute;left:0;top:430px;width:340px;height:70px;color:var(--white);text-align:center}
  .web-text .cta{font:600 16px/20px "Titillium Web",sans-serif;margin-top:12px;letter-spacing:-.2px;white-space:nowrap}
  .web-text .url{display:flex;justify-content:center;align-items:center;gap:8px;font:600 16px "Open Sans",sans-serif;margin-top:6px;letter-spacing:.4px}
  .stamp-box{position:absolute;left:595px;top:32px;width:85px;height:75px;border:1.5px solid var(--line)}
  .address-line{position:absolute;left:410px;width:270px;height:1.5px;background:var(--line)}
</style>
</head>
<body>
<div class="canvas">

  <section class="card card--front">
    <svg class="shapes" width="700" height="500" viewBox="0 0 700 500">
      <defs>
        <radialGradient id="blueBurst" cx="0.35" cy="0.45" r="0.8">
          <stop offset="0" stop-color="#3a63c8"/>
          <stop offset="1" stop-color="#0f2a6b"/>
        </radialGradient>
        <radialGradient id="photoFill" cx="0.5" cy="0.45" r="0.6">
          <stop offset="0" stop-color="#b07a45"/>
          <stop offset="0.55" stop-color="#9aa58c"/>
          <stop offset="1" stop-color="#c9cdbf"/>
        </radialGradient>
      </defs>
      <path d="M0 0H700V220Q500 340 320 330Q110 325 0 316Z" fill="url(#blueBurst)"/>
      <path d="M0 316Q110 325 320 330" fill="none" stroke="var(--red)" stroke-width="4"/>
      <circle cx="510" cy="225" r="222" fill="var(--red)"/>
      <circle cx="510" cy="225" r="207" fill="var(--white)"/>
      <circle cx="510" cy="225" r="201" fill="url(#photoFill)" role="img" aria-label="Photo of a grinning dog with ears up in front of a pile of dollar bills"/>
      <path d="M380 340H650L655 372H375Z" fill="var(--red)" stroke="var(--white)" stroke-width="2"/>
      <line x1="0" y1="453" x2="700" y2="453" stroke="var(--navy)" stroke-width="2"/>
    </svg>
    <h1 class="headline">THINKING<br>ABOUT SELING?</h1>
    <div class="headline-rule"></div>
    <p class="offer">Special Offer for<br>Arizona Homeowners</p>
    <p class="offer-agent">with: Milo Trask</p>
    <p class="cash-banner">ITS TIME TO CASH IN</p>
    <div class="brand brand--front"><span class="brand-mark"></span>Saguaro Crest Realty</div>
    <div class="socials"><span></span><span></span><span></span></div>
    <div class="contact-bar">
      <span class="item"><svg class="icon" viewBox="0 0 16 16"><circle cx="8" cy="8" r="7.5" fill="none" stroke="#fff"/><rect x="4" y="5" width="8" height="6" fill="#fff"/></svg>milotrask@brevlo.com</span>
      <span class="item"><svg class="icon" viewBox="0 0 16 16"><circle cx="8" cy="8" r="7.5" fill="none" stroke="#fff"/><path d="M5 4l2 0 1 2-1 1q1 2 3 3l1-1 2 1v2q-5 0-8-8z" fill="#fff"/></svg>(480) 555 0147</span>
      <span class="item"><svg class="icon" viewBox="0 0 16 16"><circle cx="8" cy="8" r="7.5" fill="none" stroke="#fff"/><circle cx="8" cy="8" r="4" fill="none" stroke="#fff"/><line x1="4" y1="8" x2="12" y2="8" stroke="#fff"/></svg>www.Milotrask.com</span>
    </div>
  </section>

  <section class="card card--back">
    <div class="back-photo" role="img" aria-label="Photo of a modern luxury desert home with a pool"></div>
    <div class="agent-panel"></div>
    <div class="web-bar"></div>
    <svg class="shapes" width="700" height="500" viewBox="0 0 700 500">
      <path d="M458 0H700V500H356Q334 400 340 290Q356 120 458 0Z" fill="var(--white)"/>
      <path d="M458 0Q356 120 340 290Q334 400 356 500" fill="none" stroke="var(--red)" stroke-width="4"/>
    </svg>
    <div class="agent-photo" role="img" aria-label="Portrait of the agent in a dark suit"></div>
    <h2 class="pitch">LIST YOUR<br>HOUSE FOR SALE<br>WITH ME</h2>
    <p class="agent-name">Milo Trask</p>
    <div class="agent-contact">
      <span class="item"><svg class="icon" viewBox="0 0 16 16"><circle cx="8" cy="8" r="7" fill="none" stroke="#2a4fb0" stroke-width="1.5"/><path d="M5 4l2 0 1 2-1 1q1 2 3 3l1-1 2 1v2q-5 0-8-8z" fill="#2a4fb0"/></svg>(480) 555 0147</span>
      <span class="item"><svg class="icon" viewBox="0 0 16 16"><circle cx="8" cy="8" r="7" fill="none" stroke="#2a4fb0" stroke-width="1.5"/><rect x="4" y="5" width="8" height="6" fill="#2a4fb0"/></svg>milotrask@brevlo.com</span>
    </div>
    <div class="badges"><span class="badge-wide"></span><span class="badge-square"></span></div>
    <div class="web-text">
      <p class="cta">VISIT OUR WEBSITE FOR MORE INFORMATION</p>
      <p class="url"><svg class="icon" viewBox="0 0 16 16"><circle cx="8" cy="8" r="7" fill="none" stroke="#fff" stroke-width="1.5"/><path d="M9 7l5 5-2 0-1 2z" fill="#fff"/></svg>www.Milotrask.com</p>
    </div>
    <div class="brand brand--back"><span class="brand-mark"></span>Saguaro Crest Realty</div>
    <div class="stamp-box"></div>
    <div class="address-line" style="top:188px"></div>
    <div class="address-line" style="top:237px"></div>
    <div class="address-line" style="top:286px"></div>
    <div class="address-line" style="top:335px"></div>
  </section>

</div>
</body>
</html>
```